Stationary/Business Card for Maple Freight Hauling Company
Maple Freight
Professional
Dana R Whitcomb
Managing Partner
Maple Freight LLC
4172 Old Harbor Lane
Jacksonville, Fl 32299
dana@maplefreight-example.com
www.maplefreightlines-example.com
We are looking for stationary and business cards that can easily be printed in either black and white or color. We're open to any and all ideas. Also, just a heads up but the web address listed above is still a dummy site so it will be a bit useless for inspiration. Thank you in advance for all your hard work.

```html
<!DOCTYPE html>
<html lang="en">
<head>
<meta charset="utf-8">
<title>Maple Freight — Business Cards</title>
<link href="https://fonts.googleapis.com/css2?family=Montserrat:wght@800&family=Open+Sans:wght@400;600;700&display=swap" rel="stylesheet">
<style>
  :root {
    --backdrop: #ece8e2;
    --card: #ffffff;
    --brand-green: #3f9b45;
    --band-green: #46a04c;
    --accent-red: #d8382e;
    --ink-white: #ffffff;
    --ink-soft: #e6f3e6;
    --shadow: rgba(60, 40, 20, 0.22);
  }
  * { box-sizing: border-box; margin: 0; padding: 0; }
  html, body { width: 1200px; height: 629px; overflow: hidden; }
  body {
    background: var(--backdrop);
    font-family: "Open Sans", Arial, sans-serif;
    display: flex;
    align-items: center;
    justify-content: center;
    gap: 60px;
  }
  .card {
    position: relative;
    width: 500px;
    height: 286px;
    background: var(--card);
    box-shadow: 0 10px 26px var(--shadow);
    overflow: hidden;
  }
  .wordmark {
    display: flex;
    align-items: center;
    gap: 10px;
    font-family: "Montserrat", Arial, sans-serif;
    font-weight: 800;
    color: var(--brand-green);
    letter-spacing: -0.5px;
  }
  .wordmark-dot {
    width: 18px; height: 18px;
    border-radius: 50%;
    background: var(--accent-red);
    flex: none;
  }
  .card-front { display: flex; align-items: center; justify-content: center; }
  .card-front .wordmark { font-size: 40px; }
  .card-back .wordmark {
    position: absolute;
    top: 52px; left: 0; right: 0;
    justify-content: center;
    font-size: 32px;
  }
  .card-back .wordmark-dot { width: 14px; height: 14px; }
  .rule {
    position: absolute;
    left: 0; right: 0; top: 148px;
    height: 2px;
    background: var(--accent-red);
  }
  .band {
    position: absolute;
    left: 0; right: 0; top: 154px; bottom: 0;
    background: var(--band-green);
    color: var(--ink-white);
    padding: 16px 26px 0 172px;
  }
  .person-name { font-size: 12px; font-weight: 700; }
  .person-title { font-size: 8.5px; color: var(--ink-soft); margin-bottom: 12px; }
  .contact { display: flex; gap: 30px; font-size: 8px; line-height: 1.55; }
  .contact-col { list-style: none; }
</style>
</head>
<body>
  <section class="card card-front" aria-label="Business card front">
    <div class="wordmark"><span class="wordmark-dot"></span>Maple Freight</div>
  </section>

  <section class="card card-back" aria-label="Business card back">
    <div class="wordmark"><span class="wordmark-dot"></span>Maple Freight</div>
    <div class="rule"></div>
    <div class="band">
      <p class="person-name">Dana R Whitcomb</p>
      <p class="person-title">Managing Partner</p>
      <div class="contact">
        <ul class="contact-col address">
          <li>Maple Freight LLC</li>
          <li>4172 Old Harbor Lane</li>
          <li>Jacksonville, Fl 32299</li>
        </ul>
        <ul class="contact-col reach">
          <li>Phone: 904-555-0147</li>
          <li>Fax: 904-555-0148</li>
          <li>dana@maplefreight-example.com</li>
          <li>www.maplefreightlines-example.com</li>
        </ul>
      </div>
    </div>
  </section>
</body>
</html>
```